Business Card and Letterhead Design for Public Accounting Firm

Business card and letterhead design for a CPA Firm located in Orange County, CA. We're looking for a modern and professional design utilizing our existing logo. We'd like a clean "less is more" look, but also something that catches the eye. We provide a high level of service to our clients. Open to single or double sided business cards.

Additional info: color numbers on logo
Blue :
R 0
G 83
B 125

#00537D

Silver :

R 154
G 154
B 154

#9A9A9A

Target Market(s)

Businesses and individuals

Industry/Entity Type

Accounting

Contact Information for Business Card

Moss Whitfield & Danby LLP - 4827 Larkspur Vale Road, Irvine, CA 92614 - (949)731-2864 - mwdaccts.example

Font styles to use
Serif
Sans Serif
Other font styles liked:
• See font file uploaded

Colors
0054AA
0677BA
7BADD7
CADEEF
E8F1F8

Requirements
Nice to have
• Possibly use the font file provided which matches our logo, but adjust to be not in all caps

```html
<!DOCTYPE html>
<html lang="en">
<head>
<meta charset="utf-8">
<title>Moss Whitfield &amp; Danby LLP – Business Card</title>
<link rel="stylesheet" href="https://fonts.googleapis.com/css2?family=Cinzel:wght@500;600&family=Arimo:wght@400&display=swap">
<style>
  :root {
    --brand-blue: #00537D;
    --brand-silver: #9A9A9A;
    --card-black: #000000;
    --card-white: #FFFFFF;
    --backdrop: #B4B5B7;
    --serif: "Cinzel", "Times New Roman", serif;
    --sans: "Arimo", Arial, sans-serif;
  }
  * { margin: 0; padding: 0; box-sizing: border-box; }
  html, body { width: 1200px; height: 1200px; overflow: hidden; }
  body { background: var(--backdrop); position: relative; }

  .card {
    position: absolute;
    width: 852px;
    height: 484px;
    border-radius: 26px;
  }
  .card--back { left: 174px; top: 70px; background: var(--card-black); }
  .card--front { left: 160px; top: 638px; background: var(--card-white); }

  .firm-mark {
    position: absolute;
    left: 0; right: 0;
    display: flex;
    align-items: center;
    justify-content: center;
    gap: 22px;
  }
  .firm-mark__square { width: 30px; height: 30px; background: var(--brand-blue); flex: none; }
  .firm-mark__name {
    font-family: var(--serif);
    font-weight: 500;
    text-transform: uppercase;
    line-height: 1.08;
    letter-spacing: 0.05em;
  }
  .card--back .firm-mark { top: 264px; }
  .card--back .firm-mark__square { width: 40px; height: 40px; }
  .card--back .firm-mark__name { font-size: 38px; color: var(--brand-silver); }
  .card--front .firm-mark { top: 32px; }
  .card--front .firm-mark__name { font-size: 28px; color: var(--brand-blue); }

  .web-address {
    position: absolute;
    left: 0; right: 0; top: 422px;
    text-align: center;
    font-family: var(--sans);
    font-size: 19px;
    letter-spacing: 0.42em;
    color: var(--card-white);
  }

  .person-name {
    position: absolute;
    left: 0; right: 0; top: 168px;
    text-align: center;
    font-family: var(--serif);
    font-weight: 600;
    font-size: 46px;
    color: var(--brand-blue);
    letter-spacing: 0.02em;
  }
  .person-title {
    position: absolute;
    left: 88px; right: 92px; top: 230px;
    display: flex;
    align-items: center;
    gap: 14px;
    font-family: var(--serif);
    font-weight: 600;
    font-size: 25px;
    color: var(--brand-blue);
    letter-spacing: 0.04em;
  }
  .person-title::before, .person-title::after {
    content: "";
    flex: 1;
    height: 2px;
    background: var(--brand-blue);
  }

  .address {
    position: absolute;
    left: 0; right: 0; top: 304px;
    text-align: center;
    font-family: var(--sans);
    font-size: 24px;
    line-height: 39px;
    color: var(--brand-blue);
    font-style: normal;
  }
  .contact {
    position: absolute;
    top: 410px;
    display: flex;
    align-items: center;
    gap: 6px;
    font-family: var(--sans);
    font-size: 26px;
    color: var(--brand-blue);
  }
  .contact--phone { left: 88px; }
  .contact--email { left: 444px; }
  .contact svg { fill: var(--brand-blue); flex: none; }
</style>
</head>
<body>
  <section class="card card--back" aria-label="Card back">
    <div class="firm-mark">
      <span class="firm-mark__square"></span>
      <span class="firm-mark__name">Moss Whitfield<br>&amp; Danby LLP</span>
    </div>
    <p class="web-address">www.mwdaccts.example</p>
  </section>

  <section class="card card--front" aria-label="Card front">
    <div class="firm-mark">
      <span class="firm-mark__square"></span>
      <span class="firm-mark__name">Moss Whitfield<br>&amp; Danby LLP</span>
    </div>
    <h1 class="person-name">Laura K. Penrose</h1>
    <p class="person-title">Manager</p>
    <address class="address">4827 Larkspur Vale Road,<br>Irvine, CA 92614</address>
    <p class="contact contact--phone">
      <svg width="22" height="20" viewBox="0 0 22 20" aria-hidden="true">
        <path d="M2 6 Q11 0 20 6 L20 9 L15 9 L15 6.5 Q11 5 7 6.5 L7 9 L2 9 Z"/>
        <path d="M5 10 L17 10 L20 18 L2 18 Z"/>
      </svg>
      (949)731-2864
    </p>
    <p class="contact contact--email">
      <svg width="22" height="16" viewBox="0 0 22 16" aria-hidden="true">
        <path d="M1 1 H21 V15 H1 Z M2.5 2.5 L11 9 L19.5 2.5 Z" fill-rule="evenodd"/>
      </svg>
      office@mwdaccts.example
    </p>
  </section>
</body>
</html>
```